Business Card Design for Loft Pictures

Hi we need a business card designed for a new aerial photography business we have started, we use UAV Drones to take photos for corporate, events, real estate, local government etc , the business name is Loft Pictures Australia, we have a facebook page that might help you come up with some designs - https://www.facebook.com/loftpicturesaustralia

We need to have and editable AI file so that we can use different names and contact details. details for one of the cards as follow:

Ned Harrow
phone: 03 5521 4736
Mobile: 0431 957 284
email: ned@loftpicturez.example
web: www.loftpictures.example

have now changed: Designer Payment:Committed

Target Market(s)

We are a Aerial Photography business using Drones and UAV

Industry/Entity Type

Business

Logo Text

Loft Pictures Australia

Requirements
Must have
• Colors to match logo and be part of Loft Pictures Brand

```html
<!DOCTYPE html>
<html lang="en">
<head>
<meta charset="utf-8">
<title>Loft Pictures Australia – Business Card</title>
<link rel="stylesheet" href="https://fonts.googleapis.com/css2?family=Open+Sans:ital,wght@0,400;0,600;0,700;1,700&display=swap">
<style>
  :root {
    --canvas: #1a1a1a;
    --blue-deep: #3d5ad6;
    --blue-mid: #4f74e6;
    --blue-glow: #7fb0f0;
    --logo-grey: #c8c8c8;
    --paper: #f1f1f1;
    --ink: #1e1e1e;
    --accent: #3c8fd8;
  }
  * { box-sizing: border-box; margin: 0; padding: 0; }
  html, body { width: 1200px; height: 1200px; overflow: hidden; }
  body {
    background: var(--canvas);
    font-family: "Open Sans", Arial, sans-serif;
    position: relative;
  }
  .card {
    position: absolute;
    left: 190px;
    width: 820px;
    height: 501px;
    overflow: hidden;
  }
  .card--front { top: 70px; }
  .card--back { top: 620px; background: var(--paper); }

  .card__photo {
    position: absolute; inset: 0;
    background:
      radial-gradient(ellipse 45% 30% at 52% 18%, var(--blue-glow) 0%, rgba(127,176,240,0) 100%),
      linear-gradient(180deg, var(--blue-mid) 0%, #4868e0 45%, var(--blue-deep) 100%);
  }
  .front-logo {
    position: absolute;
    left: 0; right: 0; top: 150px;
    text-align: center;
    color: var(--logo-grey);
    font-weight: 700;
  }
  .front-logo__name { font-size: 86px; line-height: 1; letter-spacing: 2px; }
  .front-logo__region { font-size: 26px; letter-spacing: 18px; margin-top: 18px; }

  .back-logo {
    position: absolute;
    left: 44px; top: 40px;
    color: var(--ink);
    font-weight: 700;
  }
  .back-logo__name { font-size: 46px; line-height: 1; }
  .back-logo__region { font-size: 15px; letter-spacing: 11px; margin-top: 8px; }

  .contact {
    position: absolute;
    left: 430px; top: 200px;
  }
  .contact__name {
    color: var(--accent);
    font-weight: 700;
    font-style: italic;
    font-size: 30px;
    margin-bottom: 30px;
    margin-left: 40px;
  }
  .contact__list { list-style: none; }
  .contact__item {
    display: flex; align-items: center;
    font-size: 20px; color: var(--ink);
    height: 40px;
  }
  .contact__icon { width: 22px; height: 22px; margin-right: 18px; flex: none; }
</style>
</head>
<body>

<section class="card card--front">
  <div class="card__photo" role="img" aria-label="Aerial photograph of a flowering field under a soft blue sky, tinted blue"></div>
  <div class="front-logo">
    <div class="front-logo__name">LOFT PICTURES</div>
    <div class="front-logo__region">AUSTRALIA</div>
  </div>
</section>

<section class="card card--back">
  <div class="back-logo">
    <div class="back-logo__name">LOFT PICTURES</div>
    <div class="back-logo__region">AUSTRALIA</div>
  </div>

  <div class="contact">
    <p class="contact__name">Ned Harrow</p>
    <ul class="contact__list">
      <li class="contact__item">
        <svg class="contact__icon" viewBox="0 0 24 24"><path d="M7 2c-2 1-3 3-3 6 0 6 6 14 12 14 2 0 3-1 4-2l-3-4-3 1c-2-1-4-5-4-7l2-2z" fill="var(--accent)"/></svg>
        03 5521 4736
      </li>
      <li class="contact__item">
        <svg class="contact__icon" viewBox="0 0 24 24"><rect x="6" y="2" width="12" height="20" rx="2" fill="none" stroke="var(--accent)" stroke-width="2"/><circle cx="12" cy="18" r="1.2" fill="var(--accent)"/></svg>
        0431 957 284
      </li>
      <li class="contact__item">
        <svg class="contact__icon" viewBox="0 0 24 24"><rect x="2" y="5" width="20" height="14" fill="var(--accent)"/><path d="M2 5l10 8 10-8" fill="none" stroke="var(--paper)" stroke-width="1.5"/></svg>
        ned@loftpicturez.example
      </li>
      <li class="contact__item">
        <svg class="contact__icon" viewBox="0 0 24 24"><circle cx="12" cy="12" r="9" fill="none" stroke="var(--accent)" stroke-width="1.6"/><ellipse cx="12" cy="12" rx="4" ry="9" fill="none" stroke="var(--accent)" stroke-width="1.4"/><path d="M3 12h18M5 7h14M5 17h14" stroke="var(--accent)" stroke-width="1.2"/></svg>
        web: www.loftpictures.example
      </li>
    </ul>
  </div>
</section>

</body>
</html>
```